Personal Injury Law Firm Marketing Postcards

Looking for 4 different high quality graphic postcards (print on both sides of 4"x6" postcard to market a Personal Injury Lawyer (Walter Gimsby). These will be placed on cars and in stores on stands. My photo and/or stock images.... We are targeting People who have been injured in automobile accidents, motorcycle accidents, slip and fall (wet/greasy floors indoors in supermarkets, restaurants, etc., snow and ice outdoors on sidewalks) trip and fall cases on dangerous staircases. indoor/outdoor, dog bite injuries. ( I like the use of stock images of these type of injury causing accidents. You can use following language "Serving People Injured in NY & NJ" . Millions of Dollars Recovered, Free Consultation and No Fee Unless We Recover Money! Phone number to be displayed (555) 418-3062 "call or text" Available 24 hours a day 7 days per week. May also want to mention that we can take over your case from another lawyer if you are not satisfied with your current attorney. There should be a small space in corner which has a space for my marketing person to handwrite in their reference code.

Target Market(s)

18-75 years old - densely populated major city

Industry/Entity Type

Legal

Font styles to use
Other font styles liked:
• Please use logo style that I uploaded.. Please do not just cut parts of my website out and use them. Do not use LOGO from my website

Colors
0054AA
0677BA
7BADD7
CADEEF
E8F1F8
00AB8E
00BBA5
67D7C9
C6EFE9
E9F9F6

Requirements
Must have
• Professional Appearance

```html
<!DOCTYPE html>
<html lang="en">
<head>
<meta charset="utf-8">
<title>Walter Gimsby Injury Lawyer Postcard</title>
<link rel="stylesheet" href="https://fonts.googleapis.com/css2?family=Cinzel:wght@500;600&family=Oswald:wght@500&family=Montserrat:wght@400;500;600;700&family=Rubik:wght@500;700&display=swap">
<style>
:root{
  --navy:#27397a;
  --gold:#c9a86a;
  --star:#f4b400;
  --ink:#3b3b3b;
  --paper:#ffffff;
  --stage:#efefef;
}
*{margin:0;padding:0;box-sizing:border-box}
html,body{width:1200px;height:2321px;overflow:hidden;background:var(--stage)}
.card{position:absolute;left:100px;width:1000px;height:667px;background:var(--paper);overflow:hidden;box-shadow:0 6px 18px rgba(0,0,0,.18)}
.card--front{top:434px}
.card--back{top:1220px}
.card__shapes{position:absolute;inset:0;width:1000px;height:667px}
.abs{position:absolute}
.serif{font-family:"Cinzel",serif;font-weight:500}

/* front */
.firm-name{left:80px;top:48px;width:310px;text-align:center;color:var(--gold);font-family:"Cinzel",serif;font-weight:500;line-height:1.15}
.firm-name__mark{display:block;width:34px;height:34px;background:var(--gold);margin:0 auto 12px}
.firm-name__small{font-size:17px;letter-spacing:1px;display:block}
.firm-name__big{font-size:28px;display:block}
.headline{left:38px;top:205px;color:#fff}
.headline__lead{font-size:45px;letter-spacing:1px;display:block;line-height:1}
.headline__main{font-size:88px;color:var(--gold);display:block;line-height:1;margin-top:4px;font-weight:600}
.headline__place{font-size:36px;display:flex;align-items:center;gap:14px;margin-top:10px;margin-left:6px}
.offer{left:40px;top:578px;color:var(--navy)}
.offer__small{font-size:16px;font-family:"Montserrat",sans-serif;display:block}
.offer__gold{font-size:22px;font-family:"Montserrat",sans-serif;font-weight:700;color:var(--gold);display:block;line-height:1}
.offer__rule{left:200px;top:578px;width:2px;height:46px;background:var(--navy)}
.offer__free{left:216px;top:574px;font-family:"Oswald",sans-serif;font-size:40px;color:var(--navy);line-height:1}
.offer__line{left:40px;top:628px;font-family:"Montserrat",sans-serif;font-size:19px;letter-spacing:2.4px;color:var(--ink)}
.lawyer__name{left:586px;top:538px;font-family:"Cinzel",serif;font-size:28px;color:#fff;letter-spacing:.5px}
.lawyer__role{left:570px;top:577px;font-family:"Montserrat",sans-serif;font-size:18px;color:#fff}
.lawyer__call{left:570px;top:607px;font-family:"Montserrat",sans-serif;font-size:14px;font-weight:700;color:var(--navy)}
.lawyer__web{left:570px;top:630px;font-family:"Montserrat",sans-serif;font-size:17px;font-weight:700;letter-spacing:3.2px;color:var(--navy)}

/* back */
.back-title{left:38px;top:36px;color:#fff;font-family:"Cinzel",serif;font-weight:500;font-size:37px;line-height:1.1}
.areas__title{left:38px;top:172px;color:#fff;font-family:"Cinzel",serif;font-weight:500;font-size:30px}
.areas{left:36px;top:230px;display:grid;grid-template-columns:177px 143px 140px;row-gap:22px;list-style:none}
.areas li{display:flex;gap:10px;align-items:flex-start;color:#fff;font-family:"Montserrat",sans-serif;font-size:15px;line-height:1.15}
.tick{flex:none;width:17px;height:17px;margin-top:1px}
.avail{left:44px;top:388px;color:#fff;font-family:"Montserrat",sans-serif;font-size:16px}
.hours{left:42px;top:415px;width:92px;height:92px}
.seven{left:158px;top:402px;font-family:"Rubik",sans-serif;font-weight:700;font-size:112px;color:var(--gold);line-height:1}
.days{left:198px;top:424px;width:256px;height:84px;background:#fff;border-radius:6px;padding:6px 0 0 46px;font-family:"Rubik",sans-serif;font-weight:500;font-size:40px;color:var(--navy);line-height:.95}
.back-call{left:38px;top:538px;font-family:"Montserrat",sans-serif;font-size:22px;font-weight:500;color:var(--ink);display:flex;align-items:center;gap:10px}
.back-call__num{font-size:24px;color:var(--navy)}
.phone-dot{width:26px;height:26px}
.back-web{left:38px;top:572px;font-family:"Montserrat",sans-serif;font-size:34px;font-weight:600;letter-spacing:4px;color:var(--ink)}
.ref-code{left:40px;top:618px;font-family:"Montserrat",sans-serif;font-size:15px;font-weight:700;color:var(--navy)}

.review{position:absolute;font-family:"Montserrat",sans-serif;font-size:13px;line-height:1.25;color:var(--ink)}
.review__open{position:absolute;left:-38px;top:-10px;font-family:Georgia,serif;font-size:56px;color:var(--gold);line-height:1}
.review__close{display:inline-block;font-family:Georgia,serif;font-size:40px;color:var(--gold);line-height:0;vertical-align:-16px;margin-left:4px}
.review__stars{display:block;color:var(--star);font-size:19px;letter-spacing:3px;line-height:1;margin-top:6px}
.review__name{display:block;font-size:12.5px;font-weight:700;color:var(--navy);text-transform:uppercase;margin-top:3px}
</style>
</head>
<body>

<section class="card card--front" aria-label="Postcard front">
  <svg class="card__shapes" viewBox="0 0 1000 667">
    <defs>
      <linearGradient id="roadPhoto" x1="0" y1="0" x2="1" y2="1">
        <stop offset="0" stop-color="#e4e5e4"/><stop offset=".55" stop-color="#a8aca9"/><stop offset="1" stop-color="#6f7470"/>
      </linearGradient>
      <linearGradient id="thumb" x1="0" y1="0" x2="1" y2="1">
        <stop offset="0" stop-color="#9aa09a"/><stop offset="1" stop-color="#4f5552"/>
      </linearGradient>
      <linearGradient id="portrait" x1="0" y1="0" x2="0" y2="1">
        <stop offset="0" stop-color="#8a7060"/><stop offset=".4" stop-color="#3a3f52"/><stop offset="1" stop-color="#22273a"/>
      </linearGradient>
    </defs>
    <polygon role="img" aria-label="Photo of an injured cyclist sitting on the road beside a car" fill="url(#roadPhoto)" points="590,0 1000,0 1000,535 582,535 470,179"/>
    <polygon fill="var(--navy)" points="0,179 447,179 560,562 0,562"/>
    <polygon role="img" aria-label="Photo of a wrecked car" fill="url(#thumb)" points="42,427 172,427 200,537 42,537"/>
    <polygon role="img" aria-label="Photo of a motorcycle accident" fill="url(#thumb)" points="194,427 324,427 352,537 222,537"/>
    <polygon role="img" aria-label="Photo of a workplace accident with a hard hat" fill="url(#thumb)" points="346,427 502,427 532,537 374,537"/>
    <polygon fill="var(--gold)" points="567,535 1000,535 1000,667 530,667"/>
    <polygon fill="var(--navy)" points="573,536 860,536 860,572 584,572"/>
    <polygon role="img" aria-label="Portrait of lawyer Walter Gimsby in a suit" fill="url(#portrait)" points="834,330 1000,314 1000,667 848,667 840,600"/>
  </svg>

  <div class="abs firm-name">
    <span class="firm-name__mark"></span>
    <span class="firm-name__small">LAW OFFICE OF</span>
    <span class="firm-name__big">WALTER GIMSBY P.C.</span>
  </div>

  <h1 class="abs headline serif">
    <span class="headline__lead">SERVING PEOPLE</span>
    <span class="headline__main">INJURED</span>
    <span class="headline__place">
      <svg width="22" height="28" viewBox="0 0 22 28" aria-hidden="true"><path d="M11 1a8 8 0 0 0-8 8c0 6 8 13 8 13s8-7 8-13a8 8 0 0 0-8-8z" fill="none" stroke="var(--gold)" stroke-width="3"/><circle cx="11" cy="9" r="3" fill="var(--gold)"/><path d="M3 26h16" stroke="var(--gold)" stroke-width="3"/></svg>
      IN NY &amp; NJ
    </span>
  </h1>

  <div class="abs offer">
    <span class="offer__small">Millions of Dollars</span>
    <span class="offer__gold">RECOVERED</span>
  </div>
  <div class="abs offer__rule"></div>
  <div class="abs offer__free">FREE CONSULTATION</div>
  <div class="abs offer__line">and No Fee Unless We Recover Money!</div>

  <div class="abs lawyer__name">WALTER GIMSBY</div>
  <div class="abs lawyer__role">Injury Lawyer</div>
  <div class="abs lawyer__call">CALL OR TEXT &nbsp;(555) 418-3062</div>
  <div class="abs lawyer__web">www.wglawny.com</div>
</section>

<section class="card card--back" aria-label="Postcard back">
  <svg class="card__shapes" viewBox="0 0 1000 667">
    <defs>
      <linearGradient id="paperTone" x1="0" y1="0" x2="1" y2="1">
        <stop offset="0" stop-color="#ffffff"/><stop offset="1" stop-color="#f4f4f4"/>
      </linearGradient>
    </defs>
    <rect width="1000" height="667" fill="url(#paperTone)"/>
    <polygon fill="var(--gold)" points="0,0 447,0 603,321 415,667 0,667"/>
    <polygon fill="var(--navy)" points="0,150 505,150 586,321 476,528 0,528"/>
    <polygon fill="#fff" points="0,528 470,528 410,642 0,642"/>
  </svg>

  <h2 class="abs back-title">SERVING PEOPLE<br>INJURED IN NY &amp; NJ</h2>
  <h3 class="abs areas__title">PRACTICE AREAS</h3>
  <ul class="abs areas">
    <li><svg class="tick" viewBox="0 0 17 17"><circle cx="8.5" cy="8.5" r="8.5" fill="var(--gold)"/><path d="M4.5 8.8l2.6 2.6 5.2-5.4" fill="none" stroke="#fff" stroke-width="2"/></svg>Dog bites<br>/attacks</li>
    <li><svg class="tick" viewBox="0 0 17 17"><circle cx="8.5" cy="8.5" r="8.5" fill="var(--gold)"/><path d="M4.5 8.8l2.6 2.6 5.2-5.4" fill="none" stroke="#fff" stroke-width="2"/></svg>Workplace<br>accidents</li>
    <li><svg class="tick" viewBox="0 0 17 17"><circle cx="8.5" cy="8.5" r="8.5" fill="var(--gold)"/><path d="M4.5 8.8l2.6 2.6 5.2-5.4" fill="none" stroke="#fff" stroke-width="2"/></svg>Motorcycle<br>accidents</li>
    <li><svg class="tick" viewBox="0 0 17 17"><circle cx="8.5" cy="8.5" r="8.5" fill="var(--gold)"/><path d="M4.5 8.8l2.6 2.6 5.2-5.4" fill="none" stroke="#fff" stroke-width="2"/></svg>Trip and fall<br>accidents</li>
    <li><svg class="tick" viewBox="0 0 17 17"><circle cx="8.5" cy="8.5" r="8.5" fill="var(--gold)"/><path d="M4.5 8.8l2.6 2.6 5.2-5.4" fill="none" stroke="#fff" stroke-width="2"/></svg>Truck<br>accidents</li>
    <li><svg class="tick" viewBox="0 0 17 17"><circle cx="8.5" cy="8.5" r="8.5" fill="var(--gold)"/><path d="M4.5 8.8l2.6 2.6 5.2-5.4" fill="none" stroke="#fff" stroke-width="2"/></svg>Pedestrian<br>accidents</li>
    <li><svg class="tick" viewBox="0 0 17 17"><circle cx="8.5" cy="8.5" r="8.5" fill="var(--gold)"/><path d="M4.5 8.8l2.6 2.6 5.2-5.4" fill="none" stroke="#fff" stroke-width="2"/></svg>Wrongful death<br>attorneys</li>
    <li><svg class="tick" viewBox="0 0 17 17"><circle cx="8.5" cy="8.5" r="8.5" fill="var(--gold)"/><path d="M4.5 8.8l2.6 2.6 5.2-5.4" fill="none" stroke="#fff" stroke-width="2"/></svg>Slip and fall<br>accidents</li>
    <li><svg class="tick" viewBox="0 0 17 17"><circle cx="8.5" cy="8.5" r="8.5" fill="var(--gold)"/><path d="M4.5 8.8l2.6 2.6 5.2-5.4" fill="none" stroke="#fff" stroke-width="2"/></svg>Car<br>accidents</li>
  </ul>

  <div class="abs avail">Available</div>
  <svg class="abs hours" viewBox="0 0 92 92" aria-hidden="true">
    <path d="M78 30A38 38 0 1 1 62 12" fill="none" stroke="var(--gold)" stroke-width="4"/>
    <path d="M58 4l8 9-11 4z" fill="var(--gold)"/>
    <text x="6" y="54" font-family="Oswald, sans-serif" font-size="44" fill="var(--gold)">24</text>
    <text x="6" y="80" font-family="Oswald, sans-serif" font-size="20" fill="var(--gold)">HOURS</text>
  </svg>
  <div class="abs days">Days<br>Per Week</div>
  <div class="abs seven">7</div>

  <div class="abs back-call">CALL OR TEXT
    <svg class="phone-dot" viewBox="0 0 26 26" aria-hidden="true"><circle cx="13" cy="13" r="12" fill="var(--gold)"/><path d="M9 7l3 3-1.6 2a8 8 0 0 0 4 4l2-1.6 3 3-2 2c-5 0-10.4-5.4-10.4-10.4z" fill="var(--navy)"/></svg>
    <span class="back-call__num">(555) 418-3062</span>
  </div>
  <div class="abs back-web">www.wglawny.com</div>
  <div class="abs ref-code">REFERENCE CODE</div>

  <article class="review" style="left:537px;top:34px;width:432px">
    <span class="review__open">&ldquo;</span>
    <p>Injury lawyer Walter Gimsby represented me after I was seriously injured in a really bad car accident. He was always there to answer my questions, he fought like hell for me and recovered the maximum amount of money that was possible! I highly recommend him and his firm.<span class="review__close">&rdquo;</span></p>
    <span class="review__stars" style="margin-left:292px">★★★★★</span>
    <span class="review__name" style="margin-left:276px">Dilmurod Karimov</span>
  </article>

  <article class="review" style="left:588px;top:178px;width:380px">
    <span class="review__open">&ldquo;</span>
    <p>Walter took my case and was extremely professional, great with follow through, and most importantly won! Overall he was a pleasure to work with.<span class="review__close">&rdquo;</span></p>
    <span class="review__stars" style="margin-left:240px">★★★★★</span>
    <span class="review__name" style="margin-left:254px">Megan Hollis</span>
  </article>

  <article class="review" style="left:633px;top:312px;width:340px">
    <span class="review__open">&ldquo;</span>
    <p>To let you all know Walter Gimsby is a outstanding lawyer what he did for me was amazing and unexpected the work he did and his team help me out very much in past 5-6 months so yes I will recommend him to anyone who's looking for a very good lawyer he's the one I will refer so Walter Gimsby keep doing your job you doing it very well Thank you<span class="review__close">&rdquo;</span></p>
    <span class="review__stars" style="margin-left:196px">★★★★★</span>
    <span class="review__name" style="margin-left:240px">JT 2nd</span>
  </article>

  <article class="review" style="left:566px;top:524px;width:418px">
    <span class="review__open" style="left:-34px">&ldquo;</span>
    <p>Thank you Mr. Gimsby for advocating for me in this case. I was hesitant at first to pursue this case but glad I did. Thank you for handling everything virtually on your end from start to finish. I believe we met twice during this entire case, at the beginning and at the end. Everything was conveniently handled online and via email.<span class="review__close">&rdquo;</span></p>
    <span class="review__stars" style="margin-left:262px;margin-top:2px">★★★★★</span>
    <span class="review__name" style="margin-left:262px">Renata Dubois</span>
  </article>
</section>

</body>
</html>
```